Real Estate Agent - Sold Brochure

I am a Real Estate Agent who is looking for a SOLD brochure design that looks simple, sharp, classy and elegant. Over the years, I have created a business image for myself that has helped me sell a lot of top end properties with great results. "Cheerful Mara, Cheerful Buyer" is my logo and the message that I consistently portray to my clients in my area.
I am after a double-sided brochure. On the front I would like a photo of the SOLD property with a watermark "not just sold....sold for a premium". It will also have my company logo, with personal profile photo and personal logo - "Cheerful Mara, Cheerful Buyer".
On the back, I would like the client testimonial letter and the client sold photo - as well as my personal logo once again - "Cheerful Mara, Cheerful Buyer".
If you could exercise your artistic imagination as a designer and create something classy and extraordinary.
Please see attached samples of work created previously and feel free to come up with new ideas or improvements.

Additional details: Flyer size to be approx. landscape layout 240mm wide x 130mm high.

Many thanks,
Mara

Additional details: Flyer size to be approx. landscape layout 240mm wide x 130mm high. with rounded corners

```html
<!DOCTYPE html>
<html lang="en">
<head>
<meta charset="utf-8">
<title>Sold Brochure – Cheerful Mara, Cheerful Buyer</title>
<link rel="stylesheet" href="https://fonts.googleapis.com/css2?family=Oswald:wght@700&family=Raleway:wght@400;600&family=Open+Sans:wght@400&display=swap">
<style>
  :root {
    --page: #ffffff;
    --band: #ffffff;
    --ink: #2a2a2a;
    --red: #c8292b;
    --red-deep: #a81f22;
    --orange: #e58a2c;
    --gold: #d9a23a;
    --headline: #ffffff;
    --photo-sky: #6f95c4;
    --photo-roof: #4e9a86;
    --photo-brick: #9a5a3c;
    --photo-lawn: #4f7f2f;
  }
  * { margin: 0; padding: 0; box-sizing: border-box; }
  html, body { width: 1107px; height: 1200px; overflow: hidden; background: var(--page); }
  .canvas { position: relative; width: 1107px; height: 1200px; }

  .side { position: absolute; left: 0; width: 1107px; border-radius: 16px; overflow: hidden; box-shadow: 0 0 0 1px #e2e2e2; }
  .side--front { top: 0; height: 596px; }
  .side--back { top: 600px; height: 600px; background: var(--red); }

  .property-photo {
    position: absolute; left: 0; top: 0; width: 1107px; height: 526px;
    background:
      linear-gradient(180deg, var(--photo-sky) 0%, #a9c2df 18%, var(--photo-roof) 19%, #3f7f70 26%, var(--photo-brick) 27%, #7e4a32 62%, var(--photo-lawn) 70%, #3d6624 100%);
  }
  .agent-portrait {
    position: absolute; right: 0; bottom: 70px; width: 228px; height: 380px;
    background: linear-gradient(180deg, rgba(60,40,30,.85) 0%, #f3f0ec 45%, #e8e4df 100%);
    border-top-left-radius: 110px 120px;
  }

  .headline { position: absolute; left: 36px; top: 316px; font-family: "Oswald", sans-serif; font-weight: 700; color: var(--headline); text-transform: uppercase; line-height: .98; transform: rotate(-3deg); transform-origin: left top; text-shadow: 0 3px 8px rgba(0,0,0,.55); }
  .headline__line { display: block; font-size: 52px; letter-spacing: 1px; }
  .headline__line--big { font-size: 58px; }
  .headline__premium { display: block; font-size: 96px; color: var(--orange); letter-spacing: 2px; }

  .band { position: absolute; left: 0; bottom: 0; width: 1107px; background: var(--band); display: flex; align-items: center; justify-content: space-between; padding: 0 20px 0 36px; }
  .side--front .band { height: 70px; }
  .side--back .band { height: 73px; }
  .brand { display: flex; align-items: center; gap: 10px; font-family: "Raleway", sans-serif; font-weight: 600; font-size: 17px; color: var(--red-deep); letter-spacing: 1px; }
  .brand__dot { width: 34px; height: 34px; border-radius: 50%; background: var(--gold); }
  .tagline { font-family: "Raleway", sans-serif; font-weight: 400; font-size: 35px; letter-spacing: 4px; color: var(--ink); }

  .testimonial { position: absolute; left: 29px; top: 68px; font-family: "Open Sans", sans-serif; font-size: 17.5px; line-height: 23.6px; color: #fff; white-space: nowrap; }
  .testimonial p + p { margin-top: 23.6px; }
  .testimonial p.tight { margin-top: 0; }

  .sold-photo { position: absolute; left: 0; top: 0; width: 1107px; height: 527px; }
  .agent-portrait--small { position: absolute; right: 0; bottom: 73px; width: 135px; height: 250px; border-top-left-radius: 70px 80px; background: linear-gradient(180deg, rgba(60,40,30,.9) 0%, #f3f0ec 48%, #e6e2dc 100%); }
</style>
</head>
<body>
<div class="canvas">
  <section class="side side--front">
    <div class="property-photo" role="img" aria-label="Photo of the sold brick home with a green roof, front garden and lawn"></div>
    <div class="agent-portrait" role="img" aria-label="Portrait of agent Mara in a white jacket"></div>
    <h1 class="headline">
      <span class="headline__line">Not just sold</span>
      <span class="headline__line headline__line--big">Sold for a</span>
      <span class="headline__premium">Premium</span>
    </h1>
    <div class="band">
      <div class="brand"><span class="brand__dot"></span>BROOKS &amp; HALE</div>
      <div class="tagline">Cheerful Mara, Cheerful Buyer</div>
    </div>
  </section>

  <section class="side side--back">
    <div class="testimonial">
      <p>Testimonial Letter</p>
      <p>42 Willowmere Court, Ashgrove Park<br>
      After having the house on sale with various other agents and<br>
      receiving only lukewarm service and low offers we were very<br>
      impressed with your sale strategy which resulted in the best<br>
      open house we ever had and multiple good offers, some<br>
      higher than the asking price leading to us accepting a good<br>
      offer and being able to move on.</p>
      <p class="tight">We have already recommended your services to a neighbour<br>
      who is thinking of selling and would be comfortable in<br>
      recommending your services to anyone in the area thinking<br>
      of selling. It was a real pleasure to have had you represent our<br>
      interested in the sale of our house.</p>
      <p>Rosalind Merrow</p>
    </div>
    <svg class="sold-photo" viewBox="0 0 1107 527" role="img" aria-label="Photo of the happy sellers and agent Mara beside the sold sign in front of the home">
      <defs>
        <linearGradient id="soldPhotoTones" x1="0" y1="0" x2="0" y2="1">
          <stop offset="0" stop-color="#5a87c0"/>
          <stop offset=".3" stop-color="#b9cde6"/>
          <stop offset=".38" stop-color="#4f8f62"/>
          <stop offset=".58" stop-color="#7a5a42"/>
          <stop offset=".8" stop-color="#5d7d3a"/>
          <stop offset="1" stop-color="#6b6b5a"/>
        </linearGradient>
      </defs>
      <polygon points="590,100 1120,12 1120,460 632,530" fill="#ffffff"/>
      <polygon points="600,108 1120,22 1120,450 640,520" fill="url(#soldPhotoTones)"/>
    </svg>
    <div class="agent-portrait--small" role="img" aria-label="Portrait of agent Mara in a white jacket"></div>
    <div class="band">
      <div class="brand"><span class="brand__dot"></span>BROOKS &amp; HALE</div>
      <div class="tagline">Cheerful Mara, Cheerful Buyer</div>
    </div>
  </section>
</div>
</body>
</html>
```